Velmora Partners - website for real estate investment company

Create a bold, modern website that reflects Velmora’s success, professionalism, and credibility.
The design must stand out while maintaining a polished, corporate tone. (bold, but understated)
The client just created a new logo, and the website design must be in sync with the logo design. Information about the logo colors, fonts, and message are in the attached design brief.
Updates

Target Market(s)

b2b: banks, brokers, institutional partners, vendors, and property sellers.

Industry/Entity Type

real estate investment company

Number of Pages Required

1 page

Font styles to use
Sans Serif

Colors

Designer to choose colors to be used in the design.

Requirements
Must have
• 1. homepage design (psd) 2. a top banner image (psd) for a default inner page
Nice to have
• please see attached design brief
Should not have

```html
<!DOCTYPE html>
<html lang="en">
<head>
<meta charset="utf-8">
<title>Velmora Partners</title>
<link href="https://fonts.googleapis.com/css2?family=Barlow:wght@400;500;600;700;800&family=Barlow+Semi+Condensed:wght@600;700&display=swap" rel="stylesheet">
<style>
:root{
  --red:#e31e24;
  --ink:#3d3d3d;
  --dark:#4a4a4a;
  --band:#555555;
  --light:#ececec;
  --foot:#f4f4f4;
  --white:#ffffff;
  --line:#9a9a9a;
}
*{margin:0;padding:0;box-sizing:border-box}
html,body{width:1200px;height:3462px;overflow:hidden}
body{position:relative;font-family:"Barlow",sans-serif;color:var(--ink);background:var(--white)}
.abs{position:absolute}
.head{font-family:"Barlow Semi Condensed",sans-serif;font-weight:700;text-transform:uppercase;letter-spacing:.5px}
.brand{font-family:"Barlow",sans-serif;font-weight:700;color:var(--ink);letter-spacing:1px}

/* nav */
.site-nav{left:0;top:0;width:1200px;height:72px;background:var(--white)}
.site-nav .brand{left:67px;top:6px;font-size:50px;line-height:60px}
.nav-links{left:372px;top:26px;display:flex;font-size:15px;font-weight:600;color:var(--ink)}
.nav-links span{padding:0 14px;border-right:1px solid #bbb;line-height:22px}
.nav-links span:last-child{border-right:0}
.nav-links span:first-child{padding-left:8px;position:relative}
.nav-links span:first-child::before{content:"";position:absolute;left:0;top:-2px;border-top:8px solid var(--red);border-right:8px solid transparent}

/* hero */
.hero{left:0;top:72px;width:1200px;height:633px;background:linear-gradient(100deg,#4b4b4b 0%,#5a5a5a 40%,#3c4a5c 60%,#555 80%,#3a3a3a 100%)}
.hero-title{left:96px;top:240px;font-size:58px;line-height:60px;color:var(--white)}
.hero-copy{left:99px;top:370px;width:540px;padding-left:22px;border-left:4px solid var(--white);color:var(--white);font-size:20px;line-height:27px}
.scroll-mouse{left:586px;top:616px}
.pause{left:1086px;top:624px}

/* stats */
.stats{left:0;top:705px;width:1200px;height:175px;background:var(--white)}
.stat{top:30px;text-align:center}
.stat .num{font-size:36px;font-weight:600;color:var(--ink);line-height:42px;margin-top:6px}
.stat .lbl{font-size:16px;font-weight:500;letter-spacing:.5px;margin-top:6px}
.vsep{top:40px;width:1px;height:115px;background:#ccc}

/* story */
.story{left:0;top:880px;width:1200px;height:607px;background:var(--light)}
.story-photo{left:0;top:0;width:600px;height:607px;background:radial-gradient(circle at 40% 45%,#f3f3f3 0%,#d4d4d4 55%,#bdbdbd 100%)}
.sec-title{font-size:48px;line-height:50px;color:var(--ink);position:absolute}
.mark{position:absolute;width:0;height:0;border-top:18px solid var(--red);border-right:18px solid transparent}
.story .sec-title{left:624px;top:158px}
.story .rule{left:907px;top:182px;width:293px;height:1px;background:var(--line)}
.body-copy{font-size:20px;line-height:27px;color:var(--ink)}
.story .body-copy{left:628px;top:240px;width:490px}
.btn{position:absolute;display:flex;align-items:center;justify-content:center;color:var(--white);font-weight:700;text-transform:uppercase;font-size:16px;letter-spacing:.3px}
.btn.red{background:var(--red)}
.btn.grey{background:var(--dark)}

/* portfolio */
.portfolio-title{left:0;top:1530px;width:1200px;text-align:center}
.portfolio-title .sec-title{position:relative;display:inline-block}
.card{top:1608px;width:396px;height:343px}
.card .pic{height:287px}
.card .cap{height:56px;background:var(--band);color:var(--white);display:flex;align-items:center;justify-content:center;font-size:21px}

/* strategy */
.strategy-rule{left:0;top:2122px;width:96px;height:1px;background:var(--line)}
.strategy-title{left:132px;top:2098px;font-size:43px;line-height:44px}
.strategy-copy{left:132px;top:2215px;width:440px}
.frame-dark{left:930px;top:2026px;width:185px;height:294px;background:var(--dark)}
.frame-red{left:636px;top:2365px;width:121px;height:111px;background:var(--red)}
.strategy-photo{left:648px;top:2038px;width:454px;height:426px;background:linear-gradient(135deg,#6f7660 0%,#a99f8c 40%,#d9d2c4 70%,#c9b79a 100%)}

/* apart */
.apart{left:0;top:2572px;width:1200px;height:548px;background:linear-gradient(160deg,#3a3f47 0%,#5b5650 40%,#7a6650 60%,#3d434c 100%)}
.apart-title{left:0;top:168px;width:1200px;text-align:center;color:var(--white);font-size:43px}
.apart-copy{left:235px;top:232px;width:730px;text-align:center;color:var(--white)}

/* footer */
.footer{left:0;top:3120px;width:1200px;height:342px;background:var(--foot)}
.footer .vline{left:356px;top:0;width:1px;height:342px;background:#d2d2d2}
.footer .hline{left:356px;top:273px;width:844px;height:1px;background:#d2d2d2}
.footer .brand{left:100px;top:64px;font-size:56px;line-height:64px}
.contact-row{left:104px;display:flex;align-items:center;gap:10px;font-size:19px}
.f-head{font-size:18px;font-weight:600;letter-spacing:.5px;color:var(--ink)}
.field{position:absolute;background:var(--white);border:1px solid #c9c9c9;font-size:12px;font-weight:500;padding:10px 18px;color:var(--ink)}
.copyright{left:400px;top:3416px;font-size:14px}
</style>
</head>
<body>

<header class="abs site-nav">
  <div class="abs brand">VELMORA</div>
  <nav class="abs nav-links">
    <span>Home</span><span>Our Story</span><span>Investment Strategy</span><span>What Sets Us Apart</span><span>Our Portfolio</span><span>Contact</span>
  </nav>
</header>

<section class="abs hero" role="img" aria-label="Dark waterfront city skyline with glass towers and trees"></section>
<h1 class="abs head hero-title">Experience –<br>Strategy – Vision</h1>
<p class="abs hero-copy">Velmora Partners is a vertically integrated real estate investment firm with a proven four-decade track record. We acquire, reposition, and operate high-performing assets across multiple sectors — always with a focus on exceptional, risk-adjusted returns.</p>
<svg class="abs scroll-mouse" width="24" height="48" viewBox="0 0 24 48" fill="none" stroke="#fff" stroke-width="2">
  <rect x="3" y="2" width="18" height="28" rx="9"/><line x1="12" y1="8" x2="12" y2="14"/>
  <polyline points="7,34 12,39 17,34"/><polyline points="7,40 12,45 17,40"/>
</svg>
<svg class="abs pause" width="50" height="50" viewBox="0 0 50 50" fill="none" stroke="#fff" stroke-width="2">
  <circle cx="25" cy="25" r="23"/><line x1="21" y1="17" x2="21" y2="33" stroke-width="3"/><line x1="29" y1="17" x2="29" y2="33" stroke-width="3"/>
</svg>

<section class="abs stats">
  <div class="abs stat" style="left:110px;width:150px">
    <svg width="42" height="42" viewBox="0 0 42 42" fill="none" stroke="#e31e24" stroke-width="2"><rect x="2" y="6" width="38" height="34" rx="2"/><line x1="2" y1="14" x2="40" y2="14"/><line x1="11" y1="2" x2="11" y2="9"/><line x1="31" y1="2" x2="31" y2="9"/><text x="21" y="31" font-size="10" fill="#e31e24" stroke="none" text-anchor="middle" font-family="Barlow,sans-serif">1989</text></svg>
    <div class="num">1989</div>
    <div class="lbl">FOUNDED</div>
  </div>
  <div class="abs vsep" style="left:350px"></div>
  <div class="abs stat" style="left:400px;width:346px">
    <svg width="56" height="42" viewBox="0 0 56 42" fill="none" stroke="#e31e24" stroke-width="2"><rect x="2" y="12" width="52" height="28"/><polyline points="2,12 14,2 28,12 42,2 54,12"/><rect x="9" y="18" width="7" height="7"/><rect x="24" y="18" width="7" height="7"/><rect x="39" y="18" width="7" height="7"/><rect x="24" y="30" width="8" height="10"/></svg>
    <div class="num">23,000+</div>
    <div class="lbl">MULTIFAMILY &amp; HEALTHCARE UNITS</div>
  </div>
  <div class="abs vsep" style="left:795px"></div>
  <div class="abs stat" style="left:835px;width:316px">
    <svg width="46" height="46" viewBox="0 0 46 46" fill="none" stroke="#e31e24" stroke-width="2"><path d="M40 23a17 17 0 1 1-5-12"/><polyline points="35,4 35,11 28,11"/><polyline points="14,23 23,15 32,23"/><rect x="17" y="22" width="12" height="10"/></svg>
    <div class="num" style="margin-top:2px">$300+</div>
    <div class="lbl">MILLION INVESTED IN RENOVATIONS</div>
  </div>
</section>

<section class="abs story">
  <div class="abs story-photo" role="img" aria-label="Upward view of pale grey skyscrapers fading into mist"></div>
  <span class="mark" style="left:608px;top:160px"></span>
  <h2 class="sec-title head">Our Story</h2>
  <div class="abs rule"></div>
  <p class="abs body-copy">Lorem ipsum dolor sit amet, consectetur adipiscing elit, sed do eiusmod tempor incididunt ut labore et dolore magna aliqua. Quis ipsum suspendisse ultrices gravida. Risus commodo viverra maecenas accumsan lacus vel facilisis.&nbsp; tempor incididunt ut labore et dolore magna</p>
  <a class="btn red" style="left:628px;top:434px;width:166px;height:44px">Learn More</a>
</section>

<div class="abs portfolio-title">
  <span class="mark" style="left:454px;top:0"></span>
  <h2 class="sec-title head" style="padding-left:14px">Portfolio</h2>
</div>
<article class="abs card" style="left:0">
  <div class="pic" role="img" aria-label="Modern apartment block with balconies against blue sky" style="background:linear-gradient(160deg,#2d8fd6 0%,#7fb7e0 45%,#8a6a5a 70%,#c8d0d8 100%)"></div>
  <div class="cap head">Project Heading</div>
</article>
<article class="abs card" style="left:402px">
  <div class="pic" role="img" aria-label="Contemporary dark building lit warmly at dusk" style="background:linear-gradient(170deg,#2e3340 0%,#4a4a52 45%,#9a6a3a 80%,#d9903a 100%)"></div>
  <div class="cap head">Project Heading</div>
</article>
<article class="abs card" style="left:806px;width:394px">
  <div class="pic" role="img" aria-label="White modern townhouses with landscaped lawn" style="background:linear-gradient(170deg,#cfd4da 0%,#eeeeee 40%,#8a8a88 70%,#7f9460 100%)"></div>
  <div class="cap head">Project Heading</div>
</article>

<div class="abs strategy-rule"></div>
<span class="mark" style="left:103px;top:2116px;border-top-width:20px;border-right-width:20px"></span>
<h2 class="abs head strategy-title">Investment<br>Strategy</h2>
<p class="abs body-copy strategy-copy">Lorem ipsum dolor sit amet, consectetur adipiscing elit, sed do eiusmod tempor incididunt ut labore et dolore magna aliqua. Quis ipsum suspendisse ultrices gravida.</p>
<a class="btn grey" style="left:131px;top:2355px;width:188px;height:50px;font-size:18px">Learn More</a>
<div class="abs frame-dark"></div>
<div class="abs frame-red"></div>
<div class="abs strategy-photo" role="img" aria-label="Hands reviewing financial charts with a pen beside a laptop"></div>

<section class="abs apart" role="img" aria-label="Upward view of glass office towers under a sunset sky">
  <h2 class="abs head apart-title"><span style="position:relative;padding-left:8px"><span class="mark" style="left:-6px;top:-2px;border-top-width:40px;border-right-width:40px"></span><span style="position:relative">What Sets Us A Part</span></span></h2>
  <p class="abs body-copy apart-copy">Velmora Partners is a vertically integrated real estate investment firm with a proven four-decade track record. We acquire, reposition, and operate high-performing assets across multiple sectors — always with a focus on exceptional, risk-adjusted returns.</p>
  <a class="btn red" style="left:520px;top:368px;width:166px;height:45px">Learn More</a>
</section>

<footer class="abs footer">
  <div class="abs vline"></div>
  <div class="abs hline"></div>
  <div class="abs brand">VELMORA</div>
  <div class="abs contact-row" style="top:146px">
    <svg width="24" height="26" viewBox="0 0 24 26"><path d="M12 1a9 9 0 0 0-9 9c0 7 9 15 9 15s9-8 9-15a9 9 0 0 0-9-9z" fill="#3d3d3d"/><circle cx="12" cy="10" r="3.5" fill="#fff"/></svg>
    <span>Marlow Ridge, NJ</span>
  </div>
  <div class="abs contact-row" style="top:186px">
    <svg width="26" height="26" viewBox="0 0 26 26"><circle cx="13" cy="13" r="12" fill="#3d3d3d"/><rect x="7" y="9" width="12" height="8" fill="none" stroke="#fff" stroke-width="1.4"/><polyline points="7,9 13,14 19,9" fill="none" stroke="#fff" stroke-width="1.4"/></svg>
    <span>info@velmora.com</span>
  </div>

  <div class="abs f-head" style="left:423px;top:64px">CAREER INQUIRIES</div>
  <a class="btn grey" style="left:423px;top:100px;width:157px;height:37px;font-size:13px;gap:8px">
    <svg width="16" height="11" viewBox="0 0 16 11" fill="none" stroke="#fff" stroke-width="1.3"><rect x="1" y="1" width="14" height="9"/><polyline points="1,1 8,6 15,1"/></svg>Email Us</a>

  <div class="abs f-head" style="left:768px;top:62px">LEAVE MESSAGE</div>
  <div class="field" style="left:768px;top:95px;width:176px;height:36px">Name</div>
  <div class="field" style="left:952px;top:95px;width:177px;height:36px">Email</div>
  <div class="field" style="left:768px;top:140px;width:361px;height:58px">Message</div>
  <a class="btn red" style="left:768px;top:209px;width:147px;height:37px;font-size:12px">Send Message &gt;</a>
</footer>
<div class="abs copyright">Copyright © 2025 Velmora. All Right Reserved</div>

</body>
</html>
```